"Thank You" flyer design

We need a "thank you" flyer that will be sent out with all our products.
a6 size landscape,
We manufacture personalised shaped signs.
I've attached a rough idea of what we are after, but would like it to be improved upon with some artistic flare..

Side one - We would like the flyer to have a simple message - "thank you for shopping with us"

Side two - we would also like our logo and a union jack made in the UK badge and our address and contact details with our website www.lumkinprints.co.uk being the most prominent..

We are after a simple bold design what would be printed on a small a6 card that people might hopefully want to keep, so the end design needs to be pretty cool.

Industry/Entity Type

Shopping

Font styles to use
Serif
Sans Serif

```html
<!DOCTYPE html>
<html lang="en">
<head>
<meta charset="utf-8">
<title>Thank you for shopping with us</title>
<link href="https://fonts.googleapis.com/css2?family=PT+Serif&family=Open+Sans:wght@400&display=swap" rel="stylesheet">
<style>
  :root {
    --frame: #8a8a8a;
    --frame-dark: #6f6f6f;
    --paper: #dedede;
    --paper-light: #e9e9e9;
    --ink: #0d0d0d;
    --grey-text: #5b5b5b;
    --magenta: #e3198e;
    --wash-dark: #555;
    --wash-light: #8c8c8c;
  }
  html, body { margin: 0; padding: 0; overflow: hidden; background: #fff; }
  .card {
    position: relative;
    width: 1200px; height: 851px;
    background: var(--frame);
    overflow: hidden;
  }
  .card__panel {
    position: absolute;
    left: 62px; top: 55px; width: 1104px; height: 762px;
    background: linear-gradient(180deg, var(--paper-light), var(--paper) 60%, #d6d6d6);
  }
  .card__wash {
    position: absolute;
    left: 240px; top: 188px; width: 770px; height: 350px;
    border-radius: 40% 30% 35% 25% / 30% 40% 45% 35%;
    background: radial-gradient(ellipse at 55% 40%, var(--wash-dark), var(--wash-light) 75%, rgba(140,140,140,0) 100%);
    opacity: 0.9;
  }
  .card__braces { position: absolute; left: 0; top: 0; }
  .message {
    position: absolute; margin: 0; white-space: nowrap;
    font-family: "PT Serif", Georgia, serif;
    color: var(--grey-text);
    font-size: 64px; line-height: 1;
  }
  .message--lead { left: 66px; top: 112px; }
  .message--tail { left: 926px; top: 557px; }
  .message__keyword {
    position: absolute; margin: 0; left: 176px; top: 285px;
    font-family: "Open Sans", Arial, sans-serif;
    font-weight: 400; font-size: 158px; line-height: 1;
    color: var(--ink); letter-spacing: 1px;
  }
  .card__bag {
    position: absolute; left: 878px; top: 470px; width: 66px; height: 90px;
    background: linear-gradient(180deg, #9a9a9a, #7a7a7a);
  }
  .web-box {
    position: absolute; left: 315px; top: 715px; width: 512px; height: 104px;
    box-sizing: border-box; border: 14px solid var(--frame-dark);
    border-bottom: none; opacity: 0.85;
  }
  .web-address {
    position: absolute; left: 330px; top: 748px; width: 482px;
    text-align: center; margin: 0;
    font-family: "PT Serif", Georgia, serif;
    font-size: 47px; line-height: 1; color: var(--magenta);
  }
</style>
</head>
<body>
  <main class="card">
    <div class="card__panel"></div>
    <div class="card__wash" role="img" aria-label="Grey watercolour brush stroke behind the headline"></div>

    <svg class="card__braces" width="1200" height="851" viewBox="0 0 1200 851" aria-hidden="true">
      <path d="M232 240 C185 240 170 255 170 300 L170 345 C170 375 150 388 105 390 C150 392 170 405 170 435 L170 470 C170 505 185 512 240 512"
            fill="none" stroke="var(--magenta)" stroke-width="22" stroke-linecap="butt"/>
      <path d="M978 190 C1030 190 1046 205 1046 245 L1046 290 C1046 318 1062 330 1088 332 C1062 334 1046 346 1046 374 L1046 420 C1046 458 1030 466 950 466"
            fill="none" stroke="var(--magenta)" stroke-width="22" stroke-linecap="butt"/>
    </svg>

    <p class="message message--lead">thank you for</p>
    <h1 class="message__keyword">SHOPPING</h1>
    <div class="card__bag" role="img" aria-label="Small shopping bag mark"></div>
    <p class="message message--tail">with us</p>

    <div class="web-box"></div>
    <p class="web-address">lumkinprints.co.uk</p>
  </main>
</body>
</html>
```